Mobile Recording Studio needs business cards

Open to seeing a creative design, but I want to emphasis my logo and minimize the name/title and company information. Possible a fully black background on card.

My company is a mobile sound recording studio. ok to include a my trailer (actual or cartoon) on the card. My initial thought is more straight forward, but a good design will win me over.

SPECS:
CMYK color mode
High (300ppi) raster effect.
cover bleed area
please deliver: Illustrator file with layers and a pdf at completion.

Name and info for the business card:

Mitchell Garvey
ADR Mixer

email: Mitchell@TakebayDub.example

address:
418 - 6057 East Pembury
Vancouver, BC V3R 2T4

phone:
604.419.8827 office

website:
www.TakebayDub.example

FB: @TakebayDub

Instagram: @TheTakebayDub

Industry/Entity Type

Television Production

Contact Information for Business Card

Mitchell Garvey
ADR Mixer

email: Mitchell@TakebayDub.example

address:
418 - 6057 East Pembury
Vancouver, BC V3R 2T4

phone:
604.419.8827 office

website:
www.TakebayDub.example

FB: @TakebayDub

Instagram: @TheTakebayDub

Colors

Designer to choose colors to be used in the design.

Requirements
Must have
• emphasis my logo and minimize the name/title and company information.
• SPECS:
• CMYK color mode
• High (300ppi) raster effect.
• cover bleed area
• please deliver: Illustrator file with layers and a pdf at completion.
Nice to have
• maybe include the following:
• all black background or black theme
• my work trailer (actual or cartoon) refer to Instagram: @TheTakebayDub

```html
<!DOCTYPE html>
<html lang="en">
<head>
<meta charset="utf-8">
<title>Takebay Dub — Business Card</title>
<link rel="stylesheet" href="https://fonts.googleapis.com/css2?family=Montserrat:wght@400;500;600&display=swap">
<style>
  :root {
    --backdrop: #d7d8da;
    --card-black: #0e0e0e;
    --silver: #d2d2d2;
    --silver-soft: #a9a9a9;
    --text-light: #ececec;
  }
  * { margin: 0; padding: 0; box-sizing: border-box; }
  html, body {
    width: 1200px; height: 800px; overflow: hidden;
    background: var(--backdrop);
    font-family: "Montserrat", Arial, sans-serif;
  }
  .canvas { position: relative; width: 1200px; height: 800px; }
  .card {
    position: absolute; width: 600px; height: 340px;
    background: var(--card-black);
    box-shadow: 0 6px 18px rgba(0,0,0,0.25);
  }
  .card--front { left: 390px; top: 45px; display: flex; align-items: center; justify-content: center; }
  .card--back { left: 210px; top: 415px; color: var(--text-light); }

  .brand-name {
    font-weight: 600; font-size: 54px; letter-spacing: 2px;
    color: var(--silver);
  }

  .holder { position: absolute; left: 48px; top: 42px; }
  .holder__name { font-weight: 500; font-size: 19px; letter-spacing: 1px; text-transform: uppercase; }
  .holder__title { font-weight: 400; font-size: 12px; color: var(--silver-soft); margin-top: 4px; }

  .contact { position: absolute; left: 40px; top: 108px; list-style: none; font-size: 14px; line-height: 19px; }
  .contact__item { display: flex; align-items: center; gap: 7px; white-space: nowrap; }
  .contact__item--gap { margin-top: 8px; }
  .contact__icon { width: 12px; height: 12px; flex: none; }
  .contact__mark { width: 11px; height: 11px; flex: none; background: var(--silver); border-radius: 2px; }
  .contact__mark--round { border-radius: 50%; background: none; border: 1.5px solid var(--silver); }

  .address {
    position: absolute; left: 40px; top: 284px;
    font-size: 15px; letter-spacing: 0.3px; white-space: nowrap;
  }

  .trailer-art {
    position: absolute; left: 345px; top: 95px; width: 225px; height: 170px;
    background: linear-gradient(160deg, #3a3a3a 0%, #1c1c1c 60%, #2c2c2c 100%);
    border-radius: 4px;
  }
</style>
</head>
<body>
<main class="canvas">
  <section class="card card--front">
    <h1 class="brand-name">Takebay Dub</h1>
  </section>

  <section class="card card--back">
    <header class="holder">
      <p class="holder__name">Mitchell Garvey</p>
      <p class="holder__title">ADR Mixer</p>
    </header>

    <ul class="contact">
      <li class="contact__item">
        <svg class="contact__icon" viewBox="0 0 24 24" aria-hidden="true"><path fill="#d2d2d2" d="M6.6 10.8a15.1 15.1 0 0 0 6.6 6.6l2.2-2.2c.3-.3.7-.4 1-.2 1.1.4 2.3.6 3.6.6.6 0 1 .4 1 1V20c0 .6-.4 1-1 1A17 17 0 0 1 3 4c0-.6.4-1 1-1h3.5c.6 0 1 .4 1 1 0 1.3.2 2.5.6 3.6.1.3 0 .7-.2 1z"/></svg>
        <span>604.419.8827 office</span>
      </li>
      <li class="contact__item">
        <svg class="contact__icon" viewBox="0 0 24 24" aria-hidden="true"><rect x="2" y="5" width="20" height="14" fill="none" stroke="#d2d2d2" stroke-width="2"/><path d="M2 5l10 8 10-8" fill="none" stroke="#d2d2d2" stroke-width="2"/></svg>
        <span>Mitchell@TakebayDub.example</span>
      </li>
      <li class="contact__item">
        <svg class="contact__icon" viewBox="0 0 24 24" aria-hidden="true"><circle cx="12" cy="12" r="9.5" fill="none" stroke="#d2d2d2" stroke-width="2"/><path d="M2.5 12h19M12 2.5c3 3 3 16 0 19M12 2.5c-3 3-3 16 0 19" fill="none" stroke="#d2d2d2" stroke-width="1.6"/></svg>
        <span>www.TakebayDub.example</span>
      </li>
      <li class="contact__item contact__item--gap">
        <span class="contact__mark"></span>
        <span>@TakebayDub</span>
      </li>
      <li class="contact__item">
        <span class="contact__mark contact__mark--round"></span>
        <span>@TheTakebayDub</span>
      </li>
    </ul>

    <div class="trailer-art" role="img" aria-label="Silver line sketch of the mobile recording studio trailer with the company name on its side"></div>

    <p class="address">418 - 6057 East Pembury, Vancouver, BC V3R 2T4</p>
  </section>
</main>
</body>
</html>
```